Logo + Label Design (Men’s Grooming Brand & Product Packaging)

Design a logo and 2 oz pomade label for Brant, a modern men’s grooming brand focused on clean, high-quality, natural ingredients. The design should establish a bold, masculine, minimalist identity that can later extend to products like shaving gel and body wash.

Key Requirements

Create a primary logo for “Brant” and a core label for the 2 oz pomade jar (screw-top).

Use a clean, modern style — masculine, confident, and approachable (think Wendel’s, Valto, Northfield Mill).

Design for 1–2 color screen printing on solid jar colors (white, black, or navy).

Avoid gradients, foil, or embossing. Must work in black & white.

Provide: vector logo, mockup of the 2 oz jar, color palette (CMYK/RGB/HEX), and font specs.

Winning design may lead to future projects (body wash, shave gel, skincare lines).

Font styles to use
Other font styles liked:
• We like the fonts and design concept in the attached mockup.

Requirements
Should not have
• We want to avoid too much writing or busy designs. We want to avoid having graphics/illustrations embedded in the logo if they will cause the brand to look less classy or sophisticated. We also want the design to look simple and all-American (e.g. Pellham and Stroud, Tall Pine, The BRIM, etc). We’d like to give a Kessler & Dunmore vibe that feels classy and high end.

```html
<!DOCTYPE html>
<html lang="en">
<head>
<meta charset="utf-8">
<title>Brant Hair Pomade Label</title>
<link rel="stylesheet" href="https://fonts.googleapis.com/css2?family=Michroma&family=Poppins:wght@400;500;600&display=swap">
<style>
  :root {
    --bg-top: #c9c9c9;
    --bg-bottom: #ececec;
    --ink: #111112;
    --jar: #1c1c1e;
    --jar-edge: #2a2a2d;
    --blue: #2aa9e2;
    --white: #f4f4f4;
    --muted: #cfcfcf;
  }
  * { box-sizing: border-box; margin: 0; padding: 0; }
  html, body { width: 1200px; height: 912px; overflow: hidden; }
  body {
    background: linear-gradient(180deg, var(--bg-top), var(--bg-bottom));
    font-family: "Poppins", sans-serif;
    position: relative;
  }
  .brand-wordmark {
    position: absolute; top: 62px; left: 0; width: 1200px;
    text-align: center;
    font-family: "Michroma", sans-serif;
    font-size: 74px; letter-spacing: 10px; color: var(--ink);
  }
  .lid-label {
    position: absolute; left: 445px; top: 200px;
    width: 310px; height: 310px; border-radius: 50%;
    background: var(--jar);
    display: flex; align-items: center; justify-content: center;
  }
  .lid-ring {
    position: absolute; inset: 12px; border-radius: 50%;
    border: 3px solid var(--blue);
  }
  .lid-content {
    position: relative; width: 230px;
    text-align: center; color: var(--white); font-family: "Michroma", sans-serif;
  }
  .lid-name { font-size: 36px; letter-spacing: 3px; line-height: 1; }
  .lid-product { font-size: 17px; letter-spacing: 2px; margin-top: 12px; }
  .lid-scent {
    display: inline-block; background: var(--blue); color: var(--jar);
    font-size: 13px; letter-spacing: 1.5px; padding: 3px 10px; margin-top: 8px;
  }
  .lid-spec { font-size: 8.5px; letter-spacing: 1px; margin-top: 12px; white-space: nowrap; }
  .lid-weight { font-size: 8.5px; letter-spacing: 1.5px; margin-top: 9px; }

  .side-label {
    position: absolute; left: 70px; top: 580px;
    width: 1060px; height: 190px; border-radius: 14px;
    background: var(--jar);
    border-top: 2px solid var(--jar-edge);
    display: grid; grid-template-columns: 1.3fr 1fr 1fr 1.1fr;
    align-items: center; padding: 0 30px; color: var(--white);
  }
  .panel { padding: 0 20px; }
  .panel + .panel { border-left: 2px solid var(--blue); }
  .panel-heading { color: var(--blue); font-weight: 600; font-size: 10px; text-transform: uppercase; }
  .panel-copy { font-size: 9.5px; line-height: 1.45; color: var(--muted); margin-bottom: 10px; }
  .side-logo { text-align: center; }
  .side-logo .logo-name { font-family: "Michroma", sans-serif; font-size: 40px; letter-spacing: 3px; line-height: 1; }
  .side-logo .claim {
    font-family: "Michroma", sans-serif; color: var(--blue);
    font-size: 8.5px; letter-spacing: 1px; margin-top: 12px; line-height: 1.5;
  }
  .benefits { list-style: none; font-size: 14px; line-height: 1.3; }
  .benefits li { margin: 6px 0; padding-left: 12px; position: relative; }
  .benefits li::before {
    content: ""; position: absolute; left: 0; top: 7px;
    width: 5px; height: 5px; background: var(--blue); border-radius: 50%;
  }
  .maker { text-align: right; font-size: 10px; color: var(--muted); line-height: 1.5; }
  .maker .panel-heading { margin-bottom: 2px; }
  .maker .web { color: var(--blue); font-weight: 600; }
  .social-marks { display: flex; justify-content: flex-end; gap: 6px; margin-top: 8px; }
  .social-marks span { width: 12px; height: 12px; background: var(--blue); border-radius: 2px; }
</style>
</head>
<body>
  <h1 class="brand-wordmark">BRANT</h1>

  <section class="lid-label" aria-label="Jar lid label">
    <div class="lid-ring"></div>
    <div class="lid-content">
      <div class="lid-name">BRANT</div>
      <div class="lid-product">HAIR POMADE</div>
      <div class="lid-scent">FRESH &amp; CLEAN</div>
      <div class="lid-spec">MEDIUM HOLD | MATTE FINISH</div>
      <div class="lid-weight">NET WT 2 OZ (57 G)</div>
    </div>
  </section>

  <section class="side-label" aria-label="Jar side label">
    <div class="panel">
      <p class="panel-heading">Directions:</p>
      <p class="panel-copy">Melt small amount of pomade between hands before massaging into damp hair (or dry hair for more texture). Style as desired. For external use only. Avoid contact with eyes. If irritation occurs, discontinue use.</p>
      <p class="panel-heading">Ingredients:</p>
      <p class="panel-copy">Butyrospermum Parkii (Shea Butter), Cera Alba (Beeswax), Polyglyceryl-3 Beeswax, Caprylic/Capric Triglyceride (Fractionated Coconut Oil), Tocopherol (Vitamin E), Fragrance (Parfum).</p>
    </div>
    <div class="panel side-logo">
      <div class="logo-name">BRANT</div>
      <div class="claim">FORMULATED TO MINIMIZE<br>SCALP IRRITATION</div>
    </div>
    <div class="panel">
      <ul class="benefits">
        <li>NATURALLY DERIVED PLANT &amp; BEE-BASED INGREDIENTS</li>
        <li>ALCOHOL FREE</li>
        <li>NON-IRRITATING</li>
      </ul>
    </div>
    <div class="panel maker">
      <p class="panel-heading">Manufactured by:</p>
      <p>Brant Health Products, Halden, NC 27000</p>
      <p>Visit us at <span class="web">branthealth.co</span></p>
      <div class="social-marks"><span></span><span></span><span></span><span></span></div>
    </div>
  </section>
</body>
</html>
```